Stonebay Towing Business Card

Towing
Accident towing
Mechanical breakdown
Insurance, salvage and recovery
4wd off road towing
Light & Heavy towing
8347 2516
24 hour business 7 days

Logo can be whole size on front

Industry/Entity Type

Towing/ transport

Contact Information for Business Card

The above

```html
<!DOCTYPE html>
<html lang="en">
<head>
<meta charset="utf-8">
<title>Stonebay Towing Business Card</title>
<link href="https://fonts.googleapis.com/css2?family=Poppins:wght@400;500;600&display=swap" rel="stylesheet">
<style>
  :root {
    --red: #e63946;
    --red-deep: #c8102e;
    --ink: #2b2b2b;
    --paper: #ffffff;
    --card-black: #2a2a2a;
    --backdrop: #9a969c;
  }
  * { margin: 0; padding: 0; box-sizing: border-box; }
  html, body {
    width: 1200px; height: 900px; overflow: hidden;
    background: var(--backdrop);
    font-family: "Poppins", sans-serif;
  }
  .stage {
    position: relative; width: 1200px; height: 900px;
    display: flex; flex-direction: column; align-items: center; justify-content: center; gap: 36px;
  }
  .card {
    position: relative; width: 700px; height: 400px;
    border-radius: 28px; overflow: hidden;
    box-shadow: 0 10px 24px rgba(0,0,0,.22);
  }
  .card--front { background: var(--paper); }
  .card--back { background: var(--card-black); display: flex; align-items: center; justify-content: center; }

  .front-wave { position: absolute; inset: 0; width: 100%; height: 100%; }

  .brand-name {
    font-weight: 600; color: var(--red); letter-spacing: .5px; white-space: nowrap;
  }
  .card--front .brand-name {
    position: absolute; left: 70px; top: 70px; font-size: 46px; line-height: 1;
  }
  .card--back .brand-name { font-size: 60px; }

  .services {
    position: absolute; left: 400px; top: 128px; list-style: none;
    font-size: 15px; font-weight: 500; color: var(--ink); line-height: 1.35; text-transform: uppercase;
  }
  .services li { position: relative; padding-left: 22px; }
  .services li::before {
    content: ""; position: absolute; left: 0; top: 6px;
    width: 9px; height: 9px; border-radius: 50%; background: var(--red);
  }
  .services .continued::before { display: none; }

  .phone {
    position: absolute; left: 396px; top: 272px;
    display: flex; align-items: center; gap: 8px;
    font-size: 34px; font-weight: 600; color: var(--ink); letter-spacing: 1px;
  }
  .phone svg { width: 22px; height: 22px; }

  .hours-pill {
    position: absolute; left: 384px; right: -30px; top: 324px; height: 30px;
    background: var(--red); color: var(--paper); border-radius: 15px;
    font-size: 15px; font-weight: 500; line-height: 30px; padding-left: 18px; text-transform: uppercase;
  }
</style>
</head>
<body>
<main class="stage">
  <section class="card card--front">
    <svg class="front-wave" viewBox="0 0 700 400" preserveAspectRatio="none" aria-hidden="true">
      <path d="M0 205 C120 190 230 240 330 320 C390 365 450 390 520 400 L0 400 Z" fill="var(--red)"/>
      <path d="M0 250 C110 240 210 285 300 350 C330 372 360 390 390 400 L0 400 Z" fill="var(--ink)"/>
      <path d="M0 256 C110 248 205 292 292 356 C318 375 344 390 372 400 L0 400 Z" fill="var(--paper)"/>
      <path d="M70 230 C140 228 200 250 250 280" stroke="var(--paper)" stroke-width="3" fill="none" stroke-linecap="round"/>
    </svg>

    <div class="brand-name">Stonebay Towing</div>

    <ul class="services">
      <li>Vehicle Transport</li>
      <li>Accident Towing</li>
      <li>Mechanical Breakdown</li>
      <li>Insurance, Salvage</li>
      <li class="continued">and Recovery</li>
      <li>4WD Off Road Towing</li>
      <li>Heavy Towing</li>
    </ul>

    <div class="phone">
      <svg viewBox="0 0 24 24" aria-hidden="true"><path fill="var(--red)" d="M6.6 10.8c1.4 2.8 3.8 5.1 6.6 6.6l2.2-2.2c.3-.3.7-.4 1-.2 1.1.4 2.3.6 3.6.6.6 0 1 .4 1 1V20c0 .6-.4 1-1 1C10.6 21 3 13.4 3 4c0-.6.4-1 1-1h3.5c.6 0 1 .4 1 1 0 1.3.2 2.5.6 3.6.1.3 0 .7-.2 1z"/></svg>
      <span>8347 2516</span>
    </div>

    <div class="hours-pill">24 Hours a Day, 7 Days a Week</div>
  </section>

  <section class="card card--back">
    <div class="brand-name">Stonebay Towing</div>
  </section>
</main>
</body>
</html>
```